Audio/ Video Packaging Design for a Technology company.

We need a packaging design for a bag that is 7" wide and 10" high. The design will be for a new line of audio/video products. We would like to see designs that represent a superior quality product that provides a pure connection. We want the equivalent of a nice retail bag that you would find in a store like Crest Mart. It should be a maximum of three colors. We really want something sharp, professional and eye catching, not whimsical or cartoonish. I've included a couple of examples below. I don't really like the designs of the bags, but I want you to see examples of what I'm looking for.

The company logo, which is uploaded, should be on the design. The words "audio and video products" should be either underneath the logo or to the side. Also, somewhere on the bag, we would like the words "For a Pure Connection"

The winner of this contest will likely get the opportunity for additional work as we have more products ready to launch.

Target Market(s)

resellers, consumers - men 25-60

Industry/Entity Type

It Company

Requirements
Must have
• It should be a maximum of three colors. We really want something sharp, professional and eye catching, not whimsical or cartoonish
Nice to have
• Eye-catching design. Utilize the entire bag but don't make it too busy.
Should not have
• Whimsical, cartoonish

```html
<!DOCTYPE html>
<html lang="en">
<head>
<meta charset="utf-8">
<title>Vertex Audio &amp; Video Products – Hang Tag Concepts</title>
<link rel="stylesheet" href="https://fonts.googleapis.com/css2?family=Jost:ital,wght@0,400;0,500;1,400;1,700&display=swap">
<style>
  :root {
    --page: #ffffff;
    --tag: #efefef;
    --ink: #2e3640;
    --blue: #1aa3dc;
    --blue-soft: #4aaee3;
    --teal-soft: #93d2d3;
    --slot: #ffffff;
  }
  html, body {
    margin: 0;
    padding: 0;
    width: 1200px;
    height: 849px;
    overflow: hidden;
    background: var(--page);
  }
  .board { display: block; width: 1200px; height: 849px; }
  .tag-body { fill: var(--tag); }
  .hang-slot { fill: var(--slot); }
  .version-label { font-family: "Jost", sans-serif; font-style: italic; font-size: 11px; fill: var(--ink); }
  .brand-name { font-family: "Jost", sans-serif; font-weight: 500; font-size: 78px; letter-spacing: 2px; fill: var(--ink); }
  .brand-square { fill: var(--blue); }
  .range-title { font-family: "Jost", sans-serif; font-weight: 500; font-size: 47px; letter-spacing: 1.5px; fill: var(--ink); }
  .range-title--bold { font-weight: 700; font-style: italic; font-size: 50px; letter-spacing: 1px; fill: var(--blue); }
  .tagline { font-family: "Jost", sans-serif; font-weight: 400; font-size: 26px; letter-spacing: 1px; fill: var(--ink); }
  .tagline--italic { font-style: italic; font-size: 23px; letter-spacing: 1.5px; }
  .divider { stroke: var(--ink); stroke-width: 4; stroke-linecap: round; }
</style>
</head>
<body>
<svg class="board" viewBox="0 0 1200 849" xmlns="http://www.w3.org/2000/svg">
  <defs>
    <radialGradient id="blue-glow" cx="0.35" cy="0.4" r="0.75">
      <stop offset="0" stop-color="var(--teal-soft)"/>
      <stop offset="1" stop-color="var(--blue-soft)"/>
    </radialGradient>
    <linearGradient id="decor-fade" x1="0" y1="0" x2="1" y2="1">
      <stop offset="0" stop-color="#1aa3dc"/>
      <stop offset="0.5" stop-color="#93d2d3"/>
      <stop offset="1" stop-color="#4aaee3"/>
    </linearGradient>
    <clipPath id="clip-tag-one">
      <rect x="69" y="73" width="505" height="726" rx="86"/>
    </clipPath>
    <clipPath id="clip-tag-two">
      <rect x="649" y="73" width="506" height="726" rx="86"/>
    </clipPath>
  </defs>

  <!-- Concept one -->
  <g class="tag tag--one">
    <text class="version-label" x="315" y="44" text-anchor="middle">v 1</text>
    <rect class="tag-body" x="69" y="73" width="505" height="726" rx="86"/>
    <g clip-path="url(#clip-tag-one)">
      <rect x="69" y="515" width="300" height="200" fill="url(#decor-fade)" opacity="0.85"
            role="img" aria-label="Gradient brand graphic in blue and teal"/>
    </g>
    <rect class="hang-slot" x="249" y="131" width="145" height="37" rx="15"/>
    <circle class="hang-slot" cx="321" cy="131" r="19"/>

    <rect class="brand-square" x="140" y="278" width="48" height="48"/>
    <text class="brand-name" x="243" y="330">VERTEX</text>

    <text class="range-title" x="236" y="397">AUDIO</text>
    <text class="range-title" x="236" y="445">AND VIDEO</text>
    <text class="range-title" x="236" y="493">PRODUCTS</text>

    <text class="tagline" x="159" y="754">FOR A PURE CONNECTION</text>
  </g>

  <!-- Concept two -->
  <g class="tag tag--two">
    <text class="version-label" x="902" y="44" text-anchor="middle">v 2</text>
    <rect class="tag-body" x="649" y="73" width="506" height="726" rx="86"/>
    <g clip-path="url(#clip-tag-two)">
      <circle cx="901" cy="147" r="135" fill="url(#blue-glow)"/>
    </g>
    <rect class="hang-slot" x="829" y="131" width="146" height="37" rx="15"/>
    <circle class="hang-slot" cx="901" cy="131" r="19"/>

    <rect class="brand-square" x="706" y="352" width="48" height="48"/>
    <text class="brand-name" x="814" y="403">VERTEX</text>

    <text class="range-title range-title--bold" x="901" y="501" text-anchor="middle">AUDIO &amp; VIDEO</text>
    <text class="range-title range-title--bold" x="901" y="561" text-anchor="middle">PRODUCTS</text>

    <line class="divider" x1="842" y1="633" x2="960" y2="633"/>

    <text class="tagline tagline--italic" x="919" y="727" text-anchor="middle">FOR A PURE CONNECTION</text>
  </g>
</svg>
</body>
</html>
```